M&A Advisory firm needs elegant and powerful letterhead

We need a powerful but elegant letterhead to engage with the international financial industry.

Target Market(s)

New York and International Financial Industry

Industry/Entity Type

Finance

Font styles to use
Other font styles liked:
• Poppins

Requirements
Must have
• 482 W 71st Street 14th Floor New York, NY 10157 O: +1 (212) 555 0147 F: +1 (212) 555 0182

```html
<!DOCTYPE html>
<html lang="en">
<head>
<meta charset="utf-8">
<title>Velmont Letterhead</title>
<link href="https://fonts.googleapis.com/css2?family=Poppins:wght@400;500&display=swap" rel="stylesheet">
<style>
  :root {
    --brand-blue: #0033c4;
    --brand-slate: #6e8087;
    --paper: #ffffff;
    --backdrop: #e4e4e4;
  }
  * { margin: 0; padding: 0; box-sizing: border-box; }
  html, body {
    width: 1200px; height: 1053px; overflow: hidden;
    background: var(--backdrop);
    font-family: "Poppins", sans-serif;
  }
  .letterhead {
    position: absolute; left: 308px; top: 116px;
    width: 581px; height: 822px;
    background: var(--paper);
  }
  .band { position: absolute; left: 0; width: 581px; }
  .band--top { top: 0; height: 19px; }
  .band--bottom { bottom: 0; height: 19px; }
  .brand {
    position: absolute; left: 38px; top: 44px;
    display: flex; align-items: center; gap: 12px;
  }
  .brand__dot {
    width: 30px; height: 30px; border-radius: 50%;
    background: var(--brand-blue);
  }
  .brand__name {
    font-size: 36px; font-weight: 400; line-height: 1;
    color: var(--brand-blue); letter-spacing: 0.5px;
  }
  .contact {
    position: absolute; color: var(--brand-slate);
  }
  .contact__row { display: flex; align-items: center; gap: 6px; }
  .contact__icon { width: 11px; height: 11px; flex: none; }
  .contact--phones { left: 319px; top: 45px; font-size: 7px; }
  .contact--phones .contact__row + .contact__row { margin-top: 7px; }
  .contact--address { left: 430px; top: 44px; font-size: 8.6px; line-height: 12.4px; align-items: flex-start; }
  .contact--address .contact__icon { margin-top: 1px; }
</style>
</head>
<body>
  <div class="letterhead">
    <svg class="band band--top" viewBox="0 0 581 19" aria-hidden="true">
      <polygon points="0,0 322,0 307,19 0,19" fill="var(--brand-blue)"/>
      <polygon points="328,0 581,0 581,16 316,16" fill="var(--brand-slate)"/>
    </svg>

    <header class="brand">
      <span class="brand__dot"></span>
      <span class="brand__name">VELMONT</span>
    </header>

    <div class="contact contact--phones">
      <div class="contact__row">
        <svg class="contact__icon" viewBox="0 0 11 11" aria-hidden="true">
          <rect width="11" height="11" rx="2" fill="var(--brand-blue)"/>
          <path d="M3.2 2.6c.4-.3.8-.2 1 .2l.5 1c.1.3 0 .5-.2.7l-.3.3c.3.8.9 1.4 1.7 1.7l.3-.3c.2-.2.5-.3.7-.2l1 .5c.4.2.5.6.2 1-.5.6-1.2.8-1.9.5C4.6 7.3 3.7 6.4 3 4.8c-.3-.8-.3-1.6.2-2.2z" fill="#fff"/>
        </svg>
        <span>+1 (212) 555 0147</span>
      </div>
      <div class="contact__row">
        <svg class="contact__icon" viewBox="0 0 11 11" aria-hidden="true">
          <rect width="11" height="11" rx="2" fill="var(--brand-blue)"/>
          <rect x="3.3" y="2" width="4.4" height="7" rx=".6" fill="none" stroke="#fff" stroke-width=".9"/>
          <circle cx="5.5" cy="8" r=".4" fill="#fff"/>
        </svg>
        <span>+1 (212) 555 0182</span>
      </div>
    </div>

    <address class="contact contact--address contact__row" style="font-style:normal">
      <svg class="contact__icon" viewBox="0 0 11 11" aria-hidden="true">
        <rect width="11" height="11" rx="2" fill="var(--brand-blue)"/>
        <path d="M5.5 1.8c-1.3 0-2.3 1-2.3 2.2 0 1.6 2.3 4.3 2.3 4.3s2.3-2.7 2.3-4.3c0-1.2-1-2.2-2.3-2.2z" fill="#fff"/>
        <circle cx="5.5" cy="4" r=".9" fill="var(--brand-blue)"/>
      </svg>
      <span>482 W 71st Street<br>14th Floor New York<br>NY 10157</span>
    </address>

    <svg class="band band--bottom" viewBox="0 0 581 19" aria-hidden="true">
      <polygon points="0,3 166,3 154,19 0,19" fill="var(--brand-slate)"/>
      <polygon points="175,0 581,0 581,19 160,19" fill="var(--brand-blue)"/>
    </svg>
  </div>
</body>
</html>
```